Hot optical boutique needs a very creative mag ad!

I need a magazine ad in the following size:
Full page trim size = 9” W x 10.875” H
(bleed size = 9.25” W x 11.125” H)

I attached my logo, and another ad which you can get my address, directions off of. I also attached various pictures you are to use.
The purpose of this ad is as follows: We are a high fashion store that just returned from our buying trip in Paris and want to give our customers a peek at what we bought for them.
The title could be: We got back from Paris and our 2016 collections have arrived!

Target Market(s)

Fashionistas!

Industry/Entity Type

Boutique

Font styles to use
Sans Serif

Requirements
Must have
• See in description.
Nice to have
• ?
Should not have
• ?

```html
<!DOCTYPE html>
<html lang="en">
<head>
<meta charset="utf-8">
<title>2016 Collections Have Arrived</title>
<link rel="stylesheet" href="https://fonts.googleapis.com/css2?family=Bebas+Neue&family=Kaushan+Script&family=Arimo:ital,wght@0,400;0,700;1,400&display=swap">
<style>
  :root {
    --stage: #e6e6e6;
    --red: #e11f35;
    --red-deep: #c8152a;
    --red-glow: #ef2b3d;
    --white: #ffffff;
    --ink: #111111;
    --band: #0d0d0d;
  }
  * { margin: 0; padding: 0; box-sizing: border-box; }
  html, body {
    width: 1200px; height: 1200px; overflow: hidden;
    background: var(--stage);
  }
  .ad {
    position: absolute; left: 101px; top: 0;
    width: 998px; height: 1200px;
    background: radial-gradient(ellipse at 50% 35%, var(--red-glow) 0%, var(--red) 45%, var(--red-deep) 100%);
    overflow: hidden;
  }
  .ad-base { position: absolute; left: 0; top: 0; width: 998px; height: 1200px; }
  .headline {
    position: absolute; left: 0; top: 48px; width: 100%;
    text-align: center; color: var(--white);
    font-family: "Bebas Neue", "Oswald", sans-serif;
    font-size: 74px; line-height: 60px; letter-spacing: 0.5px;
    font-weight: 400;
  }
  .hero-frames {
    position: absolute; left: 92px; top: 196px; width: 845px; height: 300px;
    border-radius: 40px;
    background: radial-gradient(ellipse at 50% 45%, rgba(236,34,48,0.9) 0%, rgba(160,16,28,0.75) 70%, rgba(110,10,20,0.0) 100%);
  }
  .arrived {
    position: absolute; left: 0; top: 440px; width: 100%;
    text-align: center; color: var(--white);
    font-family: "Kaushan Script", cursive;
    font-size: 200px; line-height: 240px; font-weight: 400;
    opacity: 0.93;
  }
  .contact {
    position: absolute; left: 126px; top: 1048px; width: 400px;
    text-align: center; color: var(--ink);
    font-family: "Arimo", Arial, sans-serif;
  }
  .phone { font-size: 56px; line-height: 58px; letter-spacing: 1px; }
  .hours { font-size: 17px; line-height: 20px; letter-spacing: 0.3px; }
  .address { font-size: 15px; line-height: 21px; font-weight: 700; }
  .landmark { font-size: 14px; line-height: 18px; font-style: italic; }
  .brand {
    position: absolute; left: 556px; top: 1108px;
    display: flex; align-items: center; gap: 12px;
    font-family: "Arimo", Arial, sans-serif; font-weight: 400;
    font-size: 31px; letter-spacing: 1px; color: var(--red);
  }
  .brand-dot { width: 18px; height: 18px; border-radius: 50%; background: var(--red); }
</style>
</head>
<body>
  <main class="ad">
    <svg class="ad-base" viewBox="0 0 998 1200">
      <defs>
        <radialGradient id="frame-blue" cx="50%" cy="50%" r="60%">
          <stop offset="0%" stop-color="#5a6ed0"/><stop offset="60%" stop-color="#d9dce6"/><stop offset="100%" stop-color="#ffffff"/>
        </radialGradient>
        <radialGradient id="frame-gold" cx="50%" cy="50%" r="60%">
          <stop offset="0%" stop-color="#b89a7c"/><stop offset="60%" stop-color="#e6ddd2"/><stop offset="100%" stop-color="#ffffff"/>
        </radialGradient>
        <radialGradient id="frame-smoke" cx="50%" cy="50%" r="60%">
          <stop offset="0%" stop-color="#6c7385"/><stop offset="60%" stop-color="#d4d7dd"/><stop offset="100%" stop-color="#ffffff"/>
        </radialGradient>
        <radialGradient id="frame-teal" cx="50%" cy="50%" r="60%">
          <stop offset="0%" stop-color="#3d8fb0"/><stop offset="60%" stop-color="#d3e2e8"/><stop offset="100%" stop-color="#ffffff"/>
        </radialGradient>
      </defs>
      <path class="lower-band" d="M0,810 Q499,690 998,810 L998,828 Q499,708 0,828 Z" fill="var(--band)"/>
      <path class="lower-panel" d="M0,828 Q499,708 998,828 L998,1200 L0,1200 Z" fill="var(--white)"/>
      <path class="divider" d="M305,723 Q499,714 694,723 Q499,732 305,723 Z" fill="var(--white)"/>
      <g class="product-circles" stroke="var(--red)" stroke-width="5">
        <circle cx="203" cy="868" r="102" fill="url(#frame-blue)" role="img" aria-label="Aviator sunglasses with blue lenses"/>
        <circle cx="398" cy="904" r="102" fill="url(#frame-gold)" role="img" aria-label="Aviator sunglasses with gold frame and brown lenses"/>
        <circle cx="598" cy="904" r="102" fill="url(#frame-smoke)" role="img" aria-label="Rimless shield sunglasses with grey gradient lens"/>
        <circle cx="794" cy="866" r="102" fill="url(#frame-teal)" role="img" aria-label="Black and blue optical frames"/>
      </g>
    </svg>

    <h1 class="headline">We got back from Paris and<br>our 2016 collections have</h1>
    <div class="hero-frames" role="img" aria-label="Red rimless shield sunglasses with black nose bridge"></div>
    <p class="arrived">arrived</p>

    <section class="contact">
      <p class="phone">555.210.4870</p>
      <p class="hours">OPEN MON-WED 10-6 • THUR-SAT 10-9</p>
      <p class="address">SHOPS AT HARBOR SQUARE ON ELM AVENUE</p>
      <p class="landmark">Next to Casa Verde and Olive Bistro</p>
    </section>

    <div class="brand"><span class="brand-dot"></span>LUMEN EYEWEAR</div>
  </main>
</body>
</html>
```